Web design for new streaming audio service

We need a homepage design for a new streaming audio service. Our company is called Olvantra, and we’re basically Vidorama for Audiobooks, Stand-Up Comedy, Lectures, Language Learning, etc. Essentially like Tunelark for everything audio EXCEPT music.
You don’t have to code the homepage (Design Only), but it should include 3 different designs to work with 1) Web; 2) Phones; 3) Tablets.
Below is a link to a mockup of the web version which gives a good idea of what elements we want. This is just a mockup and we want you to improve it.
Once you download the mockup, please refer to the more detailed instructions below:
The following outlines the design project for the Olvantra homepage. We have provided a rough mockup of the homepage layout that gives you a general idea of what we’re going for. There are a few elements that we are attached to, and many others where you have complete creative freedom to do whatever you think looks good.
The ZIP file includes the following:
* Mockup to see what we have in mind (olvantra-homepage-mockup.jpg)
* Text used (olvantra-homepage-text.txt)
* Raw image of actor (olvantra-actor1.jpg)
* Raw images for samples (olvantra-sample-[name].jpg)
Although we have only provided a mockup layout for the web version, we also need you to provide a mobile phone and a tablet version of the design also. It’s very possible the tablet version may be substantially similar to the web version, but the mobile phone version will likely be much different.
All of the raw files are included in the attached ZIP file. Please use our photographs and text as provided although cropping, sizing, etc. is flexible per the instructions below.
Display Requirements:
* Web Version - Minimum resolution 1024x768 (72 dpi) but should look good on 1920x1080 (72 dpi) - Page should be designed to scale to look acceptable in all resolutions in between.
* Phone Version - Minimum Zentro 4 - 640x960 (326 dpi) but should look good on Korvel Nimbus Q5 - 1920x1080 (441 dpi) - Page should be designed to scale to look acceptable in all resolutions and devices in between.
* Tablet Version - Minimum Pagewick Ember LX 7” - 1280x800 (216 dpi) but should also look good on a Slato Breeze - 2048x1536 (264 dpi) - Page should be designed to scale to look acceptable in all resolutions and devices in between.
Above the Fold - We want to make sure the Olvantra logo, Member Login Link, Large Photo, Headline, Price, Button, and the first row of sample images are all “Above the fold”. As a general guideline, this means 600 pixels high on a 1024x768 72 dpi web screen. This requirement is less important on Phone versions.
Top Logo Bar - We want to retain the blue bar with the Olvantra logo on the page, although we are open to a different size, shape and positioning if it greatly enhances the design. Please use the standard logo color, although you are welcome to use either the horizontal or vertical orientation of the logo based on your design.
Text color, font and size - Feel free to design the text in anyway you choose as long as the text is readable on the target platforms.
Buttons - Feel free to use any size, shape and colors for the buttons as long as they are obvious and clickable relative to the page. The only exception is the Chatterly button should follow the Chatterly color scheme and logo treatment (the mockup doesn’t seem 100% correct.)
Top Photograph - We want to retain the large photograph across the top of the screen although final shape and dimensions are flexible.
Size and shape of content samples (i.e. Audiobooks, Stand-Up Comedy, etc.) - Feel free to design the content samples in anyway you choose.
Three Sales Points (i.e. Listen on your Zentro…, All you can enjoy…, etc.) - The Three Sales Points are envisioned to each have a corresponding illustration which you should provide and have rights for. The placeholder is represented by a square next to the text. The color size and shape of these elements are flexible and can be designed in any way you choose.
Opt-in form - Feel free to design the opt-in form in anyway you choose as long as the text is readable and the interactivity is obvious on the target platforms.
Text links and copyright notice - Feel free to design the bottom of the page text links and copyright notice in anyway you choose.
Additional colors, graphic design elements, etc. - Feel free to use any additional colors, graphic design elements, etc. to support your design.

```html
<!DOCTYPE html>
<html lang="en">
<head>
<meta charset="utf-8">
<title>Olvantra – Unlimited Listening</title>
<link href="https://fonts.googleapis.com/css2?family=Montserrat:wght@400;500;600;700&display=swap" rel="stylesheet">
<style>
  :root {
    --brand: #04a9e6;
    --ink: #111111;
    --paper: #ffffff;
    --page: #ebebeb;
    --tile-navy: #1c3558;
    --tile-deep: #1a4d6e;
    --tile-teal: #22788c;
    --tile-light: #3d9aab;
    --muted: #6d6d6d;
  }
  * { box-sizing: border-box; margin: 0; padding: 0; }
  html, body { width: 727px; height: 1200px; overflow: hidden; }
  body {
    background: var(--page);
    font-family: "Montserrat", "Helvetica Neue", Arial, sans-serif;
    color: var(--ink);
    position: relative;
  }

  /* Top bar */
  .top-bar {
    position: absolute; left: 0; top: 0; width: 727px; height: 44px;
    background: var(--brand);
  }
  .brand-name {
    position: absolute; left: 72px; top: 6px;
    font-size: 27px; font-weight: 700; color: var(--paper); letter-spacing: -0.5px;
  }
  .member-login {
    position: absolute; right: 85px; top: 15px;
    font-size: 11px; font-weight: 600; color: var(--paper); letter-spacing: 0.3px;
    text-decoration: none;
  }

  /* Hero */
  .hero {
    position: absolute; left: 0; top: 44px; width: 727px; height: 164px;
    background: var(--paper); overflow: hidden;
  }
  .hero-photo {
    position: absolute; left: 270px; top: 0; width: 457px; height: 164px;
    background:
      linear-gradient(90deg, #ffffff 0%, rgba(255,255,255,0) 24%),
      linear-gradient(180deg, #ece9e4 0%, #ddd2c6 38%, #b99c86 62%, #6f7f96 82%, #3f4f6b 100%);
  }
  .hero-copy {
    position: absolute; left: 46px; top: 22px; width: 214px; text-align: center;
  }
  .hero-headline { font-size: 14.5px; font-weight: 700; line-height: 18px; letter-spacing: 0.4px; }
  .hero-price { margin-top: 15px; font-size: 14px; font-weight: 600; letter-spacing: 0.3px; }
  .trial-button {
    display: block; margin-top: 13px; width: 214px; height: 37px;
    background: var(--brand); color: var(--paper);
    font-size: 15.5px; font-weight: 500; line-height: 37px; letter-spacing: 0.3px;
    text-decoration: none;
  }
  .fine-print { margin-top: 6px; font-size: 4.5px; letter-spacing: 0.3px; }

  /* Categories */
  .section-title {
    position: absolute; left: 0; top: 279px; width: 723px; text-align: center;
    font-size: 14.5px; font-weight: 600; letter-spacing: 0.4px;
  }
  .section-title span { color: var(--brand); font-weight: 700; }

  .category-grid {
    position: absolute; left: 0; top: 323px; width: 723px; height: 394px;
    display: grid; grid-template-columns: repeat(4, 1fr); grid-template-rows: repeat(2, 1fr);
  }
  .category { position: relative; overflow: hidden; color: var(--paper); }
  .cat-fitness   { background: linear-gradient(180deg, var(--tile-teal) 0%, var(--tile-deep) 55%, var(--tile-navy) 100%); }
  .cat-comedy    { background: linear-gradient(160deg, var(--tile-deep) 0%, var(--tile-teal) 60%, var(--tile-deep) 100%); }
  .cat-bio       { background: linear-gradient(180deg, var(--tile-light) 0%, var(--tile-teal) 50%, var(--tile-deep) 100%); }
  .cat-language  { background: linear-gradient(200deg, var(--tile-navy) 0%, var(--tile-deep) 50%, var(--tile-navy) 100%); }
  .cat-audiobook { background: linear-gradient(180deg, var(--tile-deep) 0%, var(--tile-teal) 55%, var(--tile-navy) 100%); }
  .cat-celebrity { background: linear-gradient(170deg, var(--tile-light) 0%, var(--tile-teal) 45%, var(--tile-navy) 100%); }
  .cat-meditate  { background: linear-gradient(180deg, var(--tile-teal) 0%, var(--tile-light) 45%, var(--tile-deep) 100%); }
  .cat-business  { background: linear-gradient(180deg, var(--tile-navy) 0%, var(--tile-deep) 60%, var(--tile-navy) 100%); }
  .category-icon {
    position: absolute; left: 50%; top: 40px; width: 40px; height: 40px; margin-left: -20px;
    fill: none; stroke: var(--paper); stroke-width: 2; stroke-linecap: round; stroke-linejoin: round;
  }
  .category-label {
    position: absolute; left: 0; right: 0; top: 153px; text-align: center;
    font-size: 14px; font-weight: 600; line-height: 16px; letter-spacing: 0.3px;
  }
  .category.row-two .category-icon { top: 36px; }
  .category.row-two .category-label { top: 147px; }

  /* Selling points */
  .selling-points { position: absolute; left: 0; top: 772px; width: 727px; height: 50px; }
  .point { position: absolute; top: 0; display: flex; align-items: flex-start; }
  .point svg { width: 36px; height: 36px; fill: var(--brand); flex: none; }
  .point p {
    margin-left: 8px; margin-top: 5px;
    font-size: 10px; font-weight: 700; line-height: 12.5px; letter-spacing: 0.2px;
  }
  .point p em { font-style: normal; color: var(--brand); }
  .point-devices { left: 35px; }
  .point-price { left: 258px; }
  .point-price p { margin-left: 14px; }
  .point-cancel { left: 507px; }

  /* Sign-up band */
  .signup-band {
    position: absolute; left: 0; top: 865px; width: 723px; height: 171px;
    background: var(--brand); color: var(--paper);
  }
  .signup-title { position: absolute; left: 25px; top: 47px; font-size: 14px; font-weight: 600; letter-spacing: 0.5px; }
  .signup-text {
    position: absolute; left: 26px; top: 75px; width: 300px;
    font-size: 10px; font-weight: 600; line-height: 12.5px; letter-spacing: 0.2px;
  }
  .signup-note { position: absolute; left: 25px; top: 129px; font-size: 5px; font-weight: 700; color: var(--ink); }
  .signup-row {
    position: absolute; left: 339px; width: 356px; height: 29px;
    display: flex; border: 1px solid var(--paper);
    font-size: 10px; font-weight: 600; letter-spacing: 0.3px;
  }
  .signup-row.email { top: 49px; }
  .signup-row.social { top: 93px; }
  .signup-row > span {
    flex: 1; display: flex; align-items: center; justify-content: center;
  }
  .signup-row .solid { background: var(--paper); color: var(--brand); flex: 0 0 184px; }
  .signup-row .social-button { color: var(--paper); flex: 0 0 184px; gap: 5px; border-left: 1px solid var(--paper); }
  .social-mark { width: 9px; height: 9px; background: var(--paper); display: inline-block; }

  /* Footer */
  .footer-links {
    position: absolute; left: 44px; top: 1084px;
    font-family: Arial, "Helvetica Neue", sans-serif; font-size: 10.5px; color: var(--muted); letter-spacing: 0.3px;
  }
  .footer-links a { color: var(--muted); text-decoration: none; }
  .footer-links i { font-style: normal; margin: 0 5px; }
  .copyright {
    position: absolute; left: 44px; top: 1117px;
    font-family: Arial, "Helvetica Neue", sans-serif; font-size: 10.5px; color: var(--muted); letter-spacing: 0.6px;
  }
</style>
</head>
<body>

<header class="top-bar">
  <div class="brand-name">Olvantra</div>
  <a class="member-login" href="#">MEMBER LOGIN</a>
</header>

<section class="hero">
  <div class="hero-photo" role="img" aria-label="Smiling young man wearing headphones, looking at his phone"></div>
  <div class="hero-copy">
    <h1 class="hero-headline">UNLIMITED LISTENING.<br>WHEREVER YOU ARE.</h1>
    <p class="hero-price">ONLY $9.99 PER MONTH</p>
    <a class="trial-button" href="#">START YOUR FREE TRIAL</a>
    <p class="fine-print">* CREDIT CARD NOT REQUIRED</p>
  </div>
</section>

<h2 class="section-title">WHAT YOU CAN LISTEN TO ON <span>OLVANTRA</span></h2>

<section class="category-grid">
  <div class="category row-one cat-fitness" role="img" aria-label="Fitness programme cover with an athlete, tinted blue">
    <svg class="category-icon" viewBox="0 0 40 40"><circle cx="25" cy="7" r="3"/><path d="M14 14l8-2 5 6 6 1M22 12l-4 10 7 5-2 9M18 22l-5 6-7-1"/></svg>
    <div class="category-label">FITNESS<br>PROGRAMS</div>
  </div>
  <div class="category row-one cat-comedy" role="img" aria-label="Stand-up comedy album cover, tinted blue">
    <svg class="category-icon" viewBox="0 0 40 40"><path d="M6 16h6l12-7v22l-12-7H6z"/><path d="M10 24l3 8h4l-2-8M29 15c2 2 2 8 0 10M33 12c4 4 4 12 0 16"/></svg>
    <div class="category-label">STAND-UP<br>COMEDY</div>
  </div>
  <div class="category row-one cat-bio" role="img" aria-label="Memoir cover with an author portrait, tinted blue">
    <svg class="category-icon" viewBox="0 0 40 40"><path d="M11 6h22v26a3 3 0 0 1-3 3H9a3 3 0 0 1-3-3V14h5z"/><path d="M11 6v26M16 13h12M16 18h12M16 23h12M16 28h8"/></svg>
    <div class="category-label">BIOGRAPHIES<br>&amp; MEMOIRS</div>
  </div>
  <div class="category row-one cat-language" role="img" aria-label="Language course cover, tinted blue">
    <svg class="category-icon" viewBox="0 0 40 40"><path d="M2 15l18-8 18 8-18 8z"/><path d="M10 19v9c6 4 14 4 20 0v-9M36 16v10"/></svg>
    <div class="category-label">LANGUAGE<br>LEARNING</div>
  </div>
  <div class="category row-two cat-audiobook" role="img" aria-label="Noir novel audiobook cover, tinted blue">
    <svg class="category-icon" viewBox="0 0 40 40"><rect x="8" y="5" width="24" height="30" rx="2"/><path d="M13 5v30M18 12h9"/></svg>
    <div class="category-label">AUDIOBOOKS</div>
  </div>
  <div class="category row-two cat-celebrity" role="img" aria-label="Celebrity interview cover, tinted blue">
    <svg class="category-icon" viewBox="0 0 40 40"><path d="M20 3l5 11 12 1-9 8 3 12-11-6-11 6 3-12-9-8 12-1z"/></svg>
    <div class="category-label">CELEBRITY<br>INTERVIEWS</div>
  </div>
  <div class="category row-two cat-meditate" role="img" aria-label="Relaxation album cover with a misty mountain, tinted blue">
    <svg class="category-icon" viewBox="0 0 40 40"><circle cx="20" cy="9" r="4"/><path d="M20 14v10M8 32c4-6 8-8 12-8s8 2 12 8M6 34h28M12 20l8-3 8 3"/></svg>
    <div class="category-label">GUIDED<br>MEDITATIONS</div>
  </div>
  <div class="category row-two cat-business" role="img" aria-label="Business success course cover with a speaker portrait, tinted blue">
    <svg class="category-icon" viewBox="0 0 40 40"><rect x="4" y="4" width="32" height="32"/><path d="M9 28l8-9 6 5 9-12M27 12h5v5"/></svg>
    <div class="category-label">BUSINESS<br>TRAINING</div>
  </div>
</section>

<section class="selling-points">
  <div class="point point-devices">
    <svg viewBox="0 0 36 36"><rect x="10" y="3" width="16" height="30" rx="3"/><rect x="12.5" y="7" width="11" height="20" fill="#ebebeb"/><circle cx="18" cy="30" r="1.5" fill="#ebebeb"/></svg>
    <p>LISTEN ON YOUR<br><em>ZENTRO</em>, <em>SLATO</em> OR<br><em>ANDRIX</em> DEVICE.</p>
  </div>
  <div class="point point-price">
    <svg viewBox="0 0 36 36"><path d="M9 6h18l7 9-16 18L2 15z"/><path d="M2 15h32M13 6l-2 9 7 18 7-18-2-9" fill="none" stroke="#ebebeb" stroke-width="1.2"/></svg>
    <p>ALL YOU CAN ENJOY<br>FOR ONE <em>LOW</em><br>MONTHLY <em>PRICE</em>.</p>
  </div>
  <div class="point point-cancel">
    <svg viewBox="0 0 36 36"><path d="M20 3l12 4v24l-12 4z"/><path d="M2 14h9v-5l8 9-8 9v-5H2z"/></svg>
    <p>NO OBLIGATION.<br>CANCEL ANY TIME.</p>
  </div>
</section>

<section class="signup-band">
  <h3 class="signup-title">START YOUR FREE TRIAL</h3>
  <p class="signup-text">YOU WILL GET INSTANT &amp; UNLIMITED ACCESS<br>TO ALL THE MATERIAL ON OLVANTRA FOR 14 DAYS.<br>THERE IS NO OBLIGATION &amp; YOU CAN CANCEL<br>AT ANY TIME.</p>
  <p class="signup-note">* CREDIT CARD NOT REQUIRED</p>
  <div class="signup-row email">
    <span>YOUR EMAIL ADRESS</span>
    <span class="solid">GET INSTANT ACCESS</span>
  </div>
  <div class="signup-row social">
    <span>OR</span>
    <span class="social-button"><i class="social-mark"></i>SIGN UP USING CHATTERLY</span>
  </div>
</section>

<nav class="footer-links">
  <a href="#">About</a><i>|</i><a href="#">Help</a><i>|</i><a href="#">Contact Us</a><i>|</i><a href="#">Member Login</a><i>|</i><a href="#">Privacy Policy</a><i>|</i><a href="#">Terms of Service</a>
</nav>
<p class="copyright">©2014 Olvantra LLC – All Rights Reserved</p>

</body>
</html>
```